Brisbane IT support business needs our first website

Hi All,

We are after a new website design for our IT solutions and support business.The business name is Harlow Digital Systems Group, or HDSG for short. We provide a range of solutions and services within the IT space.

I would like to utilize the two colours in our business logo I have uploaded.

I understand this is initially for the design only aspect of the site, but I would like to engage the winner to finish coding the website and finalize after also.

Target Market(s)

Other businesses owners and home users.

Industry/Entity Type

Business

Requirements
Must have
• Nice clean and functional design utilizing our business colours from the logo.

```html
<!DOCTYPE html>
<html lang="en">
<head>
<meta charset="utf-8">
<title>HDSG – IT Solutions</title>
<link rel="stylesheet" href="https://fonts.googleapis.com/css2?family=Lato:wght@400;700&family=Roboto:wght@300;400;500;700&display=swap">
<style>
:root{
  --orange:#f08a24;
  --navy:#0e4d6b;
  --navy-dark:#0a3a52;
  --footer:#0f506e;
  --footer-bar:#0b3f58;
  --field:#1177a3;
  --text:#6d6d6d;
  --band:#f4f4f4;
  --line:#dcdcdc;
}
*{margin:0;padding:0;box-sizing:border-box}
html,body{width:1200px;height:2493px;overflow:hidden;background:#fff}
body{position:relative;font-family:'Roboto',sans-serif;color:var(--text)}
.abs{position:absolute}
.btn{display:inline-block;border-radius:5px;color:#fff;font:500 13px/26px 'Roboto',sans-serif;padding:0 16px;text-align:center}
.btn-orange{background:var(--orange)}
.btn-navy{background:var(--navy)}
.section-title{font:500 27px 'Roboto',sans-serif;color:var(--navy);text-align:center;width:100%}
.lead{font:300 14.6px/21px 'Roboto',sans-serif;color:var(--text);text-align:center}

/* header */
.site-header{left:0;top:0;width:1200px;height:66px;background:#fff}
.brand{left:138px;top:16px}
.brand-name{font:700 26px 'Roboto',sans-serif;color:var(--navy);letter-spacing:1px}
.main-nav{left:392px;top:24px;display:flex;gap:17px;font:400 13px 'Roboto',sans-serif;color:#333}
.socials{left:997px;top:24px;display:flex;gap:5px}
.socials span{width:11px;height:11px;border-radius:50%;background:var(--orange)}

/* hero */
.hero{left:0;top:66px;width:1200px;height:421px;background:linear-gradient(100deg,#f2eed8 0%,#d9d6c8 35%,#b9a39c 55%,#d4d2cc 75%,#e7e6e2 100%)}
.hero-title{left:138px;top:170px;font:400 44px/53px 'Lato',sans-serif;text-transform:uppercase}
.hero-title .l1{color:var(--orange)}
.hero-title .l2{color:var(--navy)}

/* about */
.about{left:0;top:530px;width:1200px}
.about .lead{width:860px;margin:20px auto 0}

/* services */
.services{left:0;top:718px;width:1200px;height:374px;background:var(--band)}
.services .section-title{position:absolute;top:42px}
.service{position:absolute;top:112px;width:200px;text-align:center}
.service h3{font:400 20px 'Roboto',sans-serif;color:var(--navy);margin-top:14px}
.service p{font:300 13px/18px 'Roboto',sans-serif;width:132px;height:72px;margin:12px auto 0}
.service .btn{margin-top:10px;font-size:12px;line-height:24px;padding:0 18px}

/* feature story */
.story-title{left:156px;top:1165px;font:400 22px/28px 'Roboto',sans-serif;color:var(--navy)}
.story-actions{left:201px;top:1236px;display:flex;gap:7px}
.story-shot{left:685px;top:1133px;width:375px;height:213px;background:linear-gradient(160deg,#7b63b4,#5a4a96 60%,#4a3f86)}
.divider{left:138px;width:922px;height:1px;background:var(--line)}

/* why choose */
.why{left:0;top:1428px;width:1200px}
.why .lead{width:860px;margin:18px auto 0}
.perk{position:absolute;top:1589px;width:105px;height:103px;background:#fff;border:1px solid #e2e2e2;box-shadow:0 3px 5px rgba(0,0,0,.08);text-align:center;padding-top:14px}
.perk::after{content:"";position:absolute;left:46px;bottom:-7px;width:12px;height:12px;background:#fff;border-right:1px solid #e2e2e2;border-bottom:1px solid #e2e2e2;transform:rotate(45deg)}
.perk p{font:400 14px/18px 'Roboto',sans-serif;color:var(--orange);margin-top:8px}

/* testimonial */
.team-photo{left:138px;top:1805px;width:284px;height:284px;background:linear-gradient(135deg,#c9c3bb,#a9a29a 50%,#d5d0ca)}
.quote{left:495px;top:1842px;width:490px;text-align:center}
.quote blockquote{font:400 21px/27px 'Roboto',sans-serif;color:#3b3b3b}
.quote cite{display:block;font:400 15px/20px 'Roboto',sans-serif;font-style:normal;color:#666;margin-top:8px}
.quote .btn{margin-top:18px;width:157px;line-height:25px}
.dots{display:flex;justify-content:center;gap:4px;margin-top:9px}
.dots span{width:14px;height:14px;border-radius:50%;background:var(--navy)}
.dots span.on{background:var(--orange)}

/* footer */
.site-footer{left:0;top:2122px;width:1200px;height:321px;background:var(--footer);color:#fff}
.site-footer h2{position:absolute;top:45px;width:100%;text-align:center;font:500 22px 'Roboto',sans-serif}
.site-footer .intro{position:absolute;top:82px;left:380px;width:440px;text-align:center;font:400 12px/16px 'Roboto',sans-serif}
.foot-col{position:absolute;top:160px;font:400 12px 'Roboto',sans-serif}
.foot-col h4{font:500 16px 'Roboto',sans-serif;margin-bottom:20px}
.foot-col li{list-style:none;line-height:27px}
.field{position:absolute;left:783px;width:277px;height:30px;background:var(--field);color:#6bb8dc;font:400 12px/30px 'Roboto',sans-serif;padding-left:8px}
.submit{position:absolute;left:969px;top:250px;width:91px;height:33px;background:var(--field);font:500 14px/33px 'Roboto',sans-serif;text-align:center}
.footer-bar{left:0;top:2443px;width:1200px;height:50px;background:var(--footer-bar)}
.footer-bar .copy{position:absolute;left:138px;top:17px;font:400 13px 'Roboto',sans-serif;color:#1d8fc2}
.footer-bar .socials{left:965px;top:16px}
.footer-bar .socials span{width:18px;height:18px;background:#1d7fae;margin-right:4px}
</style>
</head>
<body>

<header class="abs site-header">
  <div class="abs brand"><span class="brand-name">HDSG</span></div>
  <nav class="abs main-nav">
    <span>IT Support ▾</span><span>Web Design ▾</span><span>App Development ▾</span><span>It Staffing ▾</span><span>About Us</span><span>Contact Us</span>
  </nav>
  <div class="abs socials"><span></span><span></span><span></span><span></span></div>
</header>

<section class="abs hero" role="img" aria-label="Smiling man in a busy open-plan office with colleagues at computers"></section>
<h1 class="abs hero-title"><span class="l1">Our Peoples</span><br><span class="l2">Define Success</span></h1>

<section class="abs about">
  <h2 class="section-title">About Us</h2>
  <p class="lead">There are many variations of passages of Lorem Ipsum available, but the majority have suffered alteration in some form, by injected humour, or randomised words which don't look even slightly believable. If you are going to use a passage of Lorem Ipsum, you need to be sure there isn't anything embarrassing hidden in the middle of text. All the Lorem Ipsum generators on the Internet tend to repeat predefined chunks as necessary, making this the first true generator on the Internet.</p>
</section>

<section class="abs services">
  <h2 class="section-title">Our Services</h2>
  <div class="service" style="left:141px">
    <svg width="40" height="36" viewBox="0 0 40 36"><g stroke="#f08a24" stroke-width="4" stroke-linecap="round"><line x1="8" y1="6" x2="32" y2="32"/><line x1="32" y1="6" x2="8" y2="32"/></g><circle cx="8" cy="6" r="5" fill="#f08a24"/></svg>
    <h3>IT Support</h3>
    <p>Let us worry about your technology so you can focus on your business.</p>
    <span class="btn btn-orange">Read More</span>
  </div>
  <div class="service" style="left:375px">
    <svg width="66" height="36" viewBox="0 0 66 36" fill="#f08a24"><rect x="25" y="0" width="16" height="11"/><rect x="31" y="11" width="4" height="8"/><rect x="6" y="17" width="54" height="4"/><rect x="6" y="19" width="4" height="6"/><rect x="31" y="19" width="4" height="6"/><rect x="56" y="19" width="4" height="6"/><rect x="0" y="25" width="16" height="11"/><rect x="25" y="25" width="16" height="11"/><rect x="50" y="25" width="16" height="11"/></svg>
    <h3>Web Design</h3>
    <p>Make your web presence felt with a new site, redesign or update.</p>
    <span class="btn btn-orange">Portfolio</span>
  </div>
  <div class="service" style="left:615px">
    <svg width="38" height="36" viewBox="0 0 38 36"><rect x="0" y="0" width="38" height="36" rx="3" fill="#f08a24"/><g fill="#fff"><rect x="8" y="5" width="3" height="26"/><rect x="18" y="5" width="3" height="26"/><rect x="28" y="5" width="3" height="26"/><rect x="5" y="20" width="9" height="4"/><rect x="15" y="10" width="9" height="4"/><rect x="25" y="16" width="9" height="4"/></g></svg>
    <h3>APPS &amp; Software</h3>
    <p>Custom tailor your software &amp; business applications to your exact needs.</p>
    <span class="btn btn-orange">Read More</span>
  </div>
  <div class="service" style="left:852px">
    <svg width="62" height="36" viewBox="0 0 62 36" fill="#f08a24"><circle cx="12" cy="9" r="7"/><circle cx="31" cy="9" r="7"/><circle cx="50" cy="9" r="7"/><path d="M0 36v-8a10 10 0 0 1 10-10h4a10 10 0 0 1 10 10v8z"/><path d="M19 36v-8a10 10 0 0 1 10-10h4a10 10 0 0 1 10 10v8z"/><path d="M38 36v-8a10 10 0 0 1 10-10h4a10 10 0 0 1 10 10v8z"/></svg>
    <h3>IT Staffing</h3>
    <p>Staff your business with only the best information technology candidates.</p>
    <span class="btn btn-orange">Read More</span>
  </div>
</section>

<h2 class="abs story-title">Harlow Digital Systems Group<br>Builds New Nimbuspark Website and App</h2>
<div class="abs story-actions"><span class="btn btn-orange">Read More</span><span class="btn btn-navy">Other Stories</span></div>
<div class="abs story-shot" role="img" aria-label="Screenshot of the new Nimbuspark website homepage on a purple background"></div>

<div class="abs divider" style="top:1389px"></div>

<section class="abs why">
  <h2 class="section-title">Why Choose HDSG</h2>
  <p class="lead">There are many variations of passages of Lorem Ipsum available, but the majority have suffered alteration in some form, by injected humour, or randomised words which don't look even slightly believable. If you are going to use a passage of Lorem Ipsum, you need to be sure there isn't anything embarrassing hidden in the middle of text. All the Lorem Ipsum generators on the Internet tend to repeat predefined chunks as necessary, making this the first true generator.</p>
</section>

<div class="perk" style="left:166px"><svg width="22" height="22" viewBox="0 0 22 22"><circle cx="11" cy="11" r="9" fill="none" stroke="#0e4d6b" stroke-width="2.5"/><path d="M6 11l4 4 6-7" fill="none" stroke="#0e4d6b" stroke-width="2.5"/></svg><p>99% Uptime<br>Guarantee</p></div>
<div class="perk" style="left:293px"><svg width="22" height="22" viewBox="0 0 22 22" fill="none" stroke="#0e4d6b" stroke-width="3"><path d="M4 12a7 7 0 0 1 12-6"/><path d="M18 10a7 7 0 0 1-12 6"/></svg><p>Free<br>Migration</p></div>
<div class="perk" style="left:419px"><svg width="22" height="22" viewBox="0 0 22 22" fill="#0e4d6b"><rect x="1" y="2" width="13" height="10" rx="3"/><rect x="8" y="8" width="13" height="10" rx="3"/></svg><p>Live Chat<br>Support</p></div>
<div class="perk" style="left:545px"><svg width="22" height="22" viewBox="0 0 22 22" fill="#0e4d6b"><rect x="2" y="14" width="4" height="7"/><rect x="8" y="10" width="4" height="11"/><rect x="14" y="6" width="4" height="15"/><path d="M2 10l7-6 5 4 6-6" fill="none" stroke="#0e4d6b" stroke-width="2"/></svg><p>Hosting Up<br>time 99.9%</p></div>
<div class="perk" style="left:673px"><svg width="22" height="22" viewBox="0 0 22 22"><text x="7" y="14" font-family="Roboto,sans-serif" font-weight="700" font-size="15" fill="#0e4d6b">$</text><path d="M2 18h14l4-3" fill="none" stroke="#0e4d6b" stroke-width="2.5"/></svg><p>Variety of<br>Payment</p></div>
<div class="perk" style="left:801px"><svg width="22" height="22" viewBox="0 0 22 22" fill="none" stroke="#0e4d6b" stroke-width="2"><circle cx="11" cy="11" r="9"/><circle cx="11" cy="11" r="5"/><circle cx="11" cy="11" r="1.5" fill="#0e4d6b"/></svg><p>99% Uptime<br>Guarantee</p></div>
<div class="perk" style="left:927px"><svg width="22" height="22" viewBox="0 0 22 22" fill="none" stroke="#0e4d6b" stroke-width="2"><rect x="2" y="3" width="18" height="14"/><path d="M8 8l-3 2 3 2M14 8l3 2-3 2"/></svg><p>Online<br>Site Builder</p></div>

<div class="abs divider" style="top:1758px"></div>

<div class="abs team-photo" role="img" aria-label="Grid of staff portrait photos with the company name tile"></div>
<div class="abs quote">
  <blockquote>I look back at where we were a year ago and where we are now, and am truley impressed. The staff you have is absolutely notch</blockquote>
  <cite>Dalton Reeve ( Director Financial Planning &amp; Analysis ), Marlow Fields Foods, Inc.</cite>
  <span class="btn btn-orange">Meet Our Staff</span>
  <div class="dots"><span></span><span></span><span class="on"></span><span></span><span></span></div>
</div>

<footer class="abs site-footer">
  <h2>CONTACT US</h2>
  <p class="intro">Please contact us by phone or email for information regarding investments opportunities in the Telehealth/Telemedicine industry.</p>
  <div class="foot-col" style="left:138px">
    <h4>ADDRESS</h4>
    <ul><li>14 Carden Lane , Qc</li><li>H2K 3B9, Canada</li><li>Tel: 020-5512</li><li>Fax: 514-555-0187</li></ul>
  </div>
  <div class="foot-col" style="left:508px">
    <h4>SITE LINK'S</h4>
    <ul><li>Home</li><li>Services</li><li>Projects</li><li>Clients</li></ul>
  </div>
  <div class="field" style="top:160px">Full Name</div>
  <div class="field" style="top:200px">E-mail</div>
  <div class="submit">SUBMIT</div>
</footer>
<div class="abs footer-bar">
  <span class="copy">Copyright © 2014- Keystone Health</span>
  <div class="abs socials"><span></span><span></span><span></span><span></span></div>
</div>

</body>
</html>
```